Brochure Design Project

Architectural photography and virtual tour provider for local and national real estate markets. You can use my website for design and image needs. www.larchviewhomeshots.com

```html
<!DOCTYPE html>
<html lang="en">
<head>
<meta charset="utf-8">
<title>Larchview Home Shots – Trifold Brochure</title>
<link rel="stylesheet" href="https://fonts.googleapis.com/css2?family=Oswald:wght@300;400;500;600&family=Source+Sans+3:wght@400;600;700&display=swap">
<style>
:root{
  --blue:#2f5e96;
  --blue-deep:#23497a;
  --blue-title:#2b5c9a;
  --ink:#1d1d1f;
  --white:#ffffff;
  --orange:#f39a1d;
  --green:#4cb04f;
  --grey-text:#9a9a9a;
  --paper-light:#f5f5f5;
  --paper-shade:#cfcfcf;
  --backdrop:#c9c9c9;
}
*{box-sizing:border-box;margin:0;padding:0}
html,body{width:1200px;height:1200px;overflow:hidden}
body{background:var(--backdrop);position:relative;font-family:"Source Sans 3",sans-serif;color:var(--ink)}
.sheet{position:absolute;width:675px;height:525px;overflow:hidden;box-shadow:0 4px 14px rgba(0,0,0,.25)}
.sheet--outside{left:114px;top:53px}
.sheet--inside{left:410px;top:625px}
.sheet-art{position:absolute;inset:0}
.panel{position:absolute;top:0;height:525px}
.heading-thin{font-family:"Oswald",sans-serif;font-weight:300;font-size:21px;line-height:1.1}
.heading-bold{font-family:"Oswald",sans-serif;font-weight:500;font-size:22px;line-height:1.1}
.rule{height:3px;width:62px;margin-top:6px}

/* outside: includes panel */
.includes{left:0;width:229px;padding:15px 15px 0 15px;color:var(--blue-title)}
.includes .rule{background:var(--blue-title)}
.feature-list{list-style:none;margin-top:13px}
.feature-list li{display:flex;align-items:flex-start;gap:8px;font-size:12px;font-weight:600;color:var(--ink);line-height:1.25;margin-bottom:13px}
.feature-list svg{flex:0 0 16px;width:16px;height:16px;margin-top:1px}

/* outside: prep panel */
.prep{left:229px;width:222px;padding:15px 8px 0 7px;color:var(--white)}
.prep .rule{background:var(--white)}
.prep-list{list-style:none;margin:14px 0 0 12px}
.prep-list li{font-size:8.4px;line-height:1.3;margin-bottom:10px}
.brand{display:flex;align-items:center;gap:8px;font-size:13px;font-weight:400}
.brand-mark{width:14px;height:14px;border:1.5px solid currentColor}
.brand-tag{font-size:6px;font-weight:700;text-align:right;margin-top:1px}
.prep .brand-block{position:absolute;left:30px;top:425px;width:190px}
.url-box{position:absolute;background:var(--white);color:var(--blue-deep);font-weight:700;font-size:11px;text-align:center;line-height:21px}
.prep .url-box{left:19px;top:475px;width:186px;height:21px}

/* outside: cover panel */
.cover{left:451px;width:224px;color:var(--white)}
.cover .brand-block{position:absolute;left:28px;top:392px;width:185px}
.cover-headline{position:absolute;left:0;width:224px;text-align:center;font-family:"Oswald",sans-serif;color:#a7a7a7}
.cover-headline.big{top:440px;font-size:31px;font-weight:500;letter-spacing:-.3px}
.cover-headline.small{top:478px;font-size:15px;font-weight:400}
.cover-url{position:absolute;left:0;width:224px;top:498px;text-align:center;font-size:10.5px;font-weight:700;color:#f3d9a8}

/* inside panels */
.about{left:0;width:230px;padding:14px 10px 0 15px}
.how{left:230px;width:221px;padding:14px 8px 0 8px}
.packages{left:451px;width:224px;padding:12px 10px 0 14px;color:var(--white)}
.section-title{font-family:"Oswald",sans-serif;font-weight:500;font-size:17px;color:var(--blue-title);line-height:1.1}
.section-title + .rule{background:var(--blue-title);margin-top:4px;width:62px}
.about-item{display:flex;gap:6px;margin-top:12px}
.about-item svg{flex:0 0 16px;width:16px;height:12px;margin-top:2px}
.about-item h3{font-size:12.5px;font-weight:700;line-height:1.25}
.about-item p{font-size:8.2px;line-height:1.3}
.tick-list{list-style:none;margin:6px 0 0 10px}
.tick-list li{font-size:7.8px;margin-bottom:12px;padding-left:11px;position:relative}
.tick-list li::before{content:"✓";position:absolute;left:0;font-weight:700}
.about-closing{font-size:8.2px;line-height:1.3;text-align:justify;margin-top:8px}
.body-copy{font-size:9.2px;line-height:1.32;text-align:justify;margin-top:8px}
.body-copy + .body-copy{margin-top:10px}
.section-title.second{margin-top:16px}
.packages .section-title{color:#d8d8d8;font-size:17px}
.packages .rule{background:#d8d8d8;width:60px;margin-top:4px}
.pkg{margin-top:5px}
.pkg:first-of-type{margin-top:7px}
.pkg h4{font-size:8.2px;font-weight:700;line-height:1.2;color:#e4e4e4}
.pkg h4::before{content:"➤ ";font-size:7px}
.pkg p.note{font-size:6.6px;line-height:1.3;color:#cfd8e6;margin-left:9px}
.pkg ul{list-style:none}
.pkg li{font-size:6.7px;line-height:1.58;padding-left:17px;position:relative;color:#e8edf5;white-space:nowrap}
.pkg li::before{content:"✓";position:absolute;left:7px;color:#cfd8e6}
.packages .url-box{left:44px;top:502px;width:138px;height:16px;line-height:16px;font-size:8.5px}
</style>
</head>
<body>

<section class="sheet sheet--outside">
  <svg class="sheet-art" width="675" height="525" viewBox="0 0 675 525">
    <defs>
      <linearGradient id="paperFade" x1="0" x2="1">
        <stop offset="0" stop-color="var(--paper-light)"/>
        <stop offset="1" stop-color="var(--paper-shade)"/>
      </linearGradient>
      <linearGradient id="duskHome" x1="0" y1="0" x2="0" y2="1">
        <stop offset="0" stop-color="#22365e"/>
        <stop offset=".55" stop-color="#5a4a3c"/>
        <stop offset="1" stop-color="#b36b34"/>
      </linearGradient>
      <linearGradient id="villaDay" x1="0" y1="0" x2="0" y2="1">
        <stop offset="0" stop-color="#6ea4d8"/>
        <stop offset=".55" stop-color="#d8cdb8"/>
        <stop offset="1" stop-color="#3d8fa8"/>
      </linearGradient>
      <linearGradient id="orangeFade" x1="0" x2="1">
        <stop offset="0" stop-color="#f08a12"/>
        <stop offset="1" stop-color="#f7b13d"/>
      </linearGradient>
    </defs>
    <rect x="0" y="0" width="229" height="525" fill="url(#paperFade)"/>
    <path d="M0 318 Q100 250 229 295 L229 300 Q100 262 0 326Z" fill="var(--orange)"/>
    <path d="M120 265 Q190 268 229 292 L229 300 Q180 278 120 270Z" fill="var(--green)"/>
    <path d="M0 326 Q100 266 229 300 L229 525 L0 525Z" fill="url(#duskHome)" role="img" aria-label="Photo: modern home at dusk with a lit outdoor fire feature"/>
    <rect x="229" y="0" width="222" height="525" fill="var(--blue)"/>
    <rect x="451" y="0" width="224" height="525" fill="var(--green)"/>
    <path d="M451 0 L620 0 Q670 80 675 190 L675 310 Q600 340 520 360 Q470 372 451 380Z" fill="url(#villaDay)" role="img" aria-label="Photo: Mediterranean style home with pool and patio"/>
    <path d="M451 380 Q560 345 640 370 Q668 385 675 420 L675 525 L451 525Z" fill="url(#orangeFade)"/>
    <path d="M451 380 Q560 352 630 368 L640 372 Q555 358 451 392Z" fill="var(--white)" opacity=".85"/>
    <path d="M600 0 L675 0 L675 180 Q660 80 600 0Z" fill="var(--green)"/>
    <line x1="451" y1="0" x2="451" y2="525" stroke="#1e3f66" stroke-width="1"/>
    <line x1="245" y1="392" x2="440" y2="392" stroke="#9fb4cf" stroke-width="1.5"/>
  </svg>

  <div class="panel includes">
    <div class="heading-thin">All Photography Tours</div>
    <div class="heading-bold">Include:</div>
    <div class="rule"></div>
    <ul class="feature-list">
      <li><svg viewBox="0 0 16 16"><rect x="1" y="4" width="14" height="10" rx="1" fill="none" stroke="#222" stroke-width="1.3"/><circle cx="8" cy="9" r="3" fill="none" stroke="#222" stroke-width="1.3"/><rect x="5" y="2" width="5" height="2" fill="#222"/></svg>High Quality Professional Photography</li>
      <li><svg viewBox="0 0 16 16"><rect x="1" y="5" width="9" height="6" fill="none" stroke="#555" stroke-width="1.1"/><path d="M10 7h3l2 2v2h-5z" fill="none" stroke="#555" stroke-width="1.1"/><circle cx="4" cy="12" r="1.3" fill="#555"/><circle cx="12" cy="12" r="1.3" fill="#555"/></svg>100% Satisfaction Guaranteed</li>
      <li><svg viewBox="0 0 16 16"><rect x="1" y="2" width="14" height="9" fill="none" stroke="#222" stroke-width="1.3"/><path d="M8 11v3M5 14h6" stroke="#222" stroke-width="1.3"/></svg>Next Day Turnaround</li>
      <li><svg viewBox="0 0 16 16"><path d="M10 4l1.2 4.8L16 10l-4.8 1.2L10 16l-1.2-4.8L4 10l4.8-1.2z" fill="#222"/><path d="M3 0l.6 2.4L6 3l-2.4.6L3 6l-.6-2.4L0 3l2.4-.6z" fill="#222"/></svg>Professional Studio Editing</li>
      <li><svg viewBox="0 0 16 16"><path d="M1 8L8 2l7 6M3 7v8h10V7M6 15v-4h4v4" fill="none" stroke="#222" stroke-width="1.3"/></svg>Client Portal for 24 Hour Access</li>
      <li><svg viewBox="0 0 16 16"><rect x="4" y="1" width="8" height="14" rx="1.5" fill="none" stroke="#222" stroke-width="1.3"/></svg>Mobile Friendly Online Gallery</li>
    </ul>
  </div>

  <div class="panel prep">
    <div class="heading-thin">Prepare Your Home For</div>
    <div class="heading-bold">Photo Shoot</div>
    <div class="rule"></div>
    <ul class="prep-list">
      <li>Thoroughly clean whole house (vacuum carpet, mop floors, clean counter tops, clean windows)</li>
      <li>Turn all overhead lights and lamps ON</li>
      <li>Use bulbs of the same temperature (ALL incandescent or ALL compact fluorescent)</li>
      <li>Replace all burned out light bulbs</li>
      <li>Turn all ceiling fans OFF</li>
      <li>Turn all TVs OFF</li>
      <li>Turn all computer screens OFF</li>
      <li>Open blinds/window treatments to let in outside light</li>
      <li>Remove personal photographs (or replace with general landscape/object photographs)</li>
      <li>Make all beds</li>
      <li>Remove small floor rugs to reveal actual flooring</li>
      <li>Place all shoes/jackets in closet</li>
    </ul>
    <div class="brand-block">
      <div class="brand"><span class="brand-mark"></span><span>Larchview Home Shots</span></div>
      <div class="brand-tag">Become noticed...</div>
    </div>
    <div class="url-box">www.larchviewhomeshots.com</div>
  </div>

  <div class="panel cover">
    <div class="brand-block">
      <div class="brand"><span class="brand-mark"></span><span>Larchview Home Shots</span></div>
      <div class="brand-tag">Become noticed...</div>
    </div>
    <div class="cover-headline big">SELL 32% FASTER</div>
    <div class="cover-headline small">WIN MORE. SELL MORE.</div>
    <div class="cover-url">www.larchviewhomeshots.com</div>
  </div>
</section>

<section class="sheet sheet--inside">
  <svg class="sheet-art" width="675" height="525" viewBox="0 0 675 525">
    <defs>
      <linearGradient id="paperFade2" x1="0" x2="1">
        <stop offset="0" stop-color="var(--paper-light)"/>
        <stop offset="1" stop-color="var(--paper-shade)"/>
      </linearGradient>
      <linearGradient id="paperFade3" x1="0" x2="1">
        <stop offset="0" stop-color="#ffffff"/>
        <stop offset="1" stop-color="#e4e4e4"/>
      </linearGradient>
      <linearGradient id="aerialHome" x1="0" y1="0" x2="0" y2="1">
        <stop offset="0" stop-color="#8a8270"/>
        <stop offset=".5" stop-color="#4e6a6a"/>
        <stop offset="1" stop-color="#2f8fb0"/>
      </linearGradient>
      <linearGradient id="circleHome" x1="0" y1="0" x2="0" y2="1">
        <stop offset="0" stop-color="#8fb3d6"/>
        <stop offset=".5" stop-color="#c8b394"/>
        <stop offset="1" stop-color="#3c7a5a"/>
      </linearGradient>
      <linearGradient id="cityBlue" x1="0" y1="0" x2="0" y2="1">
        <stop offset="0" stop-color="#4a6f98"/>
        <stop offset=".3" stop-color="var(--blue)"/>
        <stop offset="1" stop-color="var(--blue-deep)"/>
      </linearGradient>
    </defs>
    <rect x="0" y="0" width="230" height="525" fill="url(#paperFade2)"/>
    <rect x="230" y="0" width="221" height="525" fill="url(#paperFade3)"/>
    <path d="M0 360 Q110 290 230 303 L230 310 Q110 300 0 372Z" fill="var(--green)"/>
    <path d="M0 372 Q110 305 230 310 L451 310 L451 525 L0 525Z" fill="url(#aerialHome)" role="img" aria-label="Aerial photo: contemporary hillside home with infinity pool"/>
    <circle cx="367" cy="352" r="99" fill="none" stroke="var(--orange)" stroke-width="12"/>
    <circle cx="367" cy="352" r="83" fill="var(--white)"/>
    <circle cx="367" cy="352" r="78" fill="url(#circleHome)" role="img" aria-label="Aerial photo: two-storey villa with terrace and pool"/>
    <rect x="451" y="0" width="224" height="525" fill="url(#cityBlue)"/>
    <line x1="451" y1="0" x2="451" y2="525" stroke="#e08a10" stroke-width="2"/>
  </svg>

  <div class="panel about">
    <div class="section-title">ABOUT US</div>
    <div class="rule"></div>
    <div class="about-item">
      <svg viewBox="0 0 16 12"><path d="M0 0l16 6-16 6 4-6z" fill="var(--blue-title)"/></svg>
      <div><h3>30 Years trusted<br>Experience</h3><p>Proudly serving all Southern Nevada based real estate companies.</p></div>
    </div>
    <div class="about-item">
      <svg viewBox="0 0 16 12"><path d="M0 0l16 6-16 6 4-6z" fill="var(--blue-title)"/></svg>
      <div><h3>Professional Photos</h3></div>
    </div>
    <ul class="tick-list">
      <li>Properties with quality photos sell 32% faster!</li>
      <li>Stand out against the competition.</li>
      <li>Up to 20% higher asking price per sq. ft.</li>
    </ul>
    <div class="about-item" style="margin-top:4px">
      <svg viewBox="0 0 16 12"><path d="M0 0l16 6-16 6 4-6z" fill="var(--blue-title)"/></svg>
      <div><h3>Stunning Aerial Images</h3><p>Take your listings to the next level and show case your listings like never before!</p></div>
    </div>
    <p class="about-closing">We bring the highest quality photography in a simple, elegant way. We'll handle making it look beautiful, so all you have to worry about is capturing more leads, winning more listing, and selling more properties.</p>
  </div>

  <div class="panel how">
    <div class="section-title">HOW WE DO IT</div>
    <p class="body-copy">Our trained real estate photographers will capture all interior/exterior views including amenities of your property.</p>
    <p class="body-copy">We use only the best cameras and optics available to produce results that make your property stand out and give buyers a sense of quality and attention to detail.</p>
    <div class="section-title second">BRIGHTPANE TECHNOLOGY</div>
    <div class="rule"></div>
    <p class="body-copy">Take your listings to the next level with our unique HDR BRIGHTPANE Technology. Our process digitally enhances the image through an augmentation process. The end result is sharper photos, enhanced colors and elimination of overexposed windows.</p>
  </div>

  <div class="panel packages">
    <div class="section-title">PHOTOGRAPHY PACKAGES</div>
    <div class="rule"></div>
    <div class="pkg"><h4>12 SHOT TOUR AT $105</h4><ul>
      <li>Offered on small homes and condos &lt;1200 sq ft</li>
      <li>Advanced BRIGHTPANE HDR Image processing.</li>
      <li>Professional Real Estate trained Photographer.</li>
      <li>Next Day turnaround during business hours.</li></ul></div>
    <div class="pkg"><h4>25 SHOT TOUR AT $135</h4><ul>
      <li>Recommended for properties that are 1200 -3000 sq ft</li>
      <li>Advanced BRIGHTPANE HDR Image processing.</li>
      <li>Professional Real Estate trained Photographer.</li>
      <li>Next Day turnaround during business hours.</li></ul></div>
    <div class="pkg"><h4>35 SHOT TOUR AT $155</h4><ul>
      <li>Recommended for properties that are 3000 - 5000 sq ft</li>
      <li>Advanced BRIGHTPANE HDR Image processing.</li>
      <li>Professional Real Estate trained Photographer.</li>
      <li>Next Day turnaround during business hours.</li></ul></div>
    <div class="pkg"><h4>50 SHOT TOUR AT $205</h4><ul>
      <li>Recommended for properties that are &gt;5000 sq ft</li>
      <li>Advanced BRIGHTPANE HDR Image processing.</li>
      <li>Professional Real Estate trained Photographer.</li>
      <li>Next Day Turnaround during business hours.</li></ul></div>
    <div class="pkg"><h4>35 SHOT TWILIGHT AT $275</h4><ul>
      <li>Twilight Images shot at dusk for a truly stunning effect.</li>
      <li>Advanced BRIGHTPANE HDR Image processing.</li>
      <li>Professional Real Estate trained Photographer.</li>
      <li>Next Day Turnaround during business hours.</li></ul></div>
    <div class="pkg"><h4>AERIALS SHOTS AT $150</h4><p class="note">Flight restrictions may apply.</p><ul>
      <li>6-12 low &amp; high oblique image of your home or land.</li>
      <li>Photo Shot with a LARCHVIEW certified drone pilot.</li>
      <li>Capture the beauty and perspective like never before!</li>
      <li>Next Day Turnaround during business hours.</li></ul></div>
    <div class="pkg"><h4>3D ROOMSPAN AT $200 <span style="font-weight:400">Up to 3000 sq ft</span></h4><p class="note">(Can be added any tour package)</p><ul>
      <li>3D Virtual Walk-Through</li>
      <li>3D doll house rendering of your property.</li>
      <li>$.07 cents per Sq Ft above 3000 sq ft</li>
      <li>Next Day Turnaround during business hours.</li></ul></div>
    <div class="url-box">www.larchviewhomeshots.com</div>
  </div>
</section>

</body>
</html>
```